WWW.VELTRONA.IT BUSINNES CARD

WE NEED A BUSINESS CARD . I HAVE A COMPANY IN ITALY NR 1 IN HAIR MEDICAL CARE AN HAIR REPLECEMENT . IN CARD I NEED WRITE WEB ADDRESS, MAIL , ADDRESS, TELEPHONE NUMBER , AND NAME
IN THE BACK SIDE I NEED MY DOCTOR LOGO .
MY WEB SITE IS WWW.VELTRONA.IT
Updates

Target Market(s)

CONSUMER B2C

Industry/Entity Type

Hair And Beauty

Contact Information for Business Card

I WANT A MEDICAL BUSINESS CARD.

Font styles to use
Other font styles liked:
• VERDANA

Colors
33a6d7
3176b5
85abd2
aedbee
eaf1f7
ffffff

Requirements
Must have
• I NEED MY LOGO AND LOGO OF DR VELTRONA

```html
<!DOCTYPE html>
<html lang="it">
<head>
<meta charset="utf-8">
<title>Veltrona – Business Card</title>
<link href="https://fonts.googleapis.com/css2?family=Ubuntu:ital,wght@0,400;0,500;0,700;1,700&display=swap" rel="stylesheet">
<style>
  :root {
    --navy: #0b4f9c;
    --sky: #33a6d7;
    --mid-blue: #3176b5;
    --pale-blue: #eaf1f7;
    --paper: #ffffff;
    --ink-grey: #3d3d3d;
    --stage: #d6d9dc;
    --hair-brown: #7a4524;
    --shadow-peach: #e7a57a;
  }
  * { box-sizing: border-box; margin: 0; padding: 0; }
  html, body {
    width: 1200px;
    height: 1200px;
    overflow: hidden;
    background: var(--stage);
    font-family: "Ubuntu", sans-serif;
  }
  .card {
    position: absolute;
    left: 150px;
    width: 900px;
    height: 500px;
    background: var(--paper);
    box-shadow: 0 6px 18px rgba(0,0,0,0.18);
    overflow: hidden;
  }
  .card--info { top: 70px; }
  .card--mascot { top: 630px; }

  .brand {
    position: absolute;
    display: flex;
    align-items: center;
    gap: 18px;
  }
  .brand__dot {
    width: 58px;
    height: 58px;
    border-radius: 50%;
    background: var(--sky);
  }
  .brand__name {
    font-weight: 700;
    font-size: 92px;
    line-height: 1;
    color: var(--navy);
    letter-spacing: -1px;
  }
  .tagline {
    position: absolute;
    font-size: 21px;
    font-weight: 500;
    color: var(--navy);
    letter-spacing: 1px;
    text-transform: uppercase;
  }

  /* info side */
  .card--info .brand { left: 250px; top: 60px; }
  .card--info .tagline { left: 250px; top: 170px; }
  .contact {
    position: absolute;
    left: 150px;
    top: 270px;
    display: grid;
    grid-template-columns: 40px auto;
    row-gap: 22px;
    font-size: 26px;
    color: var(--ink-grey);
    line-height: 1.25;
  }
  .contact__label {
    font-weight: 700;
    font-style: italic;
    color: var(--navy);
  }
  .online {
    position: absolute;
    left: 600px;
    top: 300px;
    font-size: 27px;
    line-height: 1.5;
    color: var(--navy);
  }

  /* mascot side */
  .card--mascot .brand { left: 60px; top: 130px; }
  .card--mascot .tagline { left: 60px; top: 240px; font-size: 19px; }
  .web-pill {
    position: absolute;
    left: 60px;
    top: 290px;
    width: 360px;
    height: 62px;
    border-radius: 14px;
    background: var(--navy);
    color: var(--paper);
    font-size: 36px;
    display: flex;
    align-items: center;
    justify-content: center;
  }
  .mascot {
    position: absolute;
    left: 520px;
    top: 0;
    width: 260px;
    height: 480px;
  }
  .doctor-name {
    position: absolute;
    left: 795px;
    top: 420px;
    transform: rotate(-90deg);
    transform-origin: left top;
    font-size: 46px;
    font-weight: 700;
    font-style: italic;
    color: var(--navy);
    white-space: nowrap;
  }
</style>
</head>
<body>

<section class="card card--info" aria-label="Business card, contact side">
  <div class="brand">
    <span class="brand__dot"></span>
    <span class="brand__name">Veltrona</span>
  </div>
  <p class="tagline">Cura e reintegrazione dei capelli</p>

  <div class="contact">
    <span class="contact__label">a</span>
    <span>via Lentisco 14<br>Verona, Italy</span>
    <span class="contact__label">t</span>
    <span>+39 045 5550192</span>
  </div>

  <div class="online">
    <p>www.veltrona.it</p>
    <p>info@veltrona.it</p>
  </div>
</section>

<section class="card card--mascot" aria-label="Business card, mascot side">
  <div class="brand">
    <span class="brand__dot"></span>
    <span class="brand__name">Veltrona</span>
  </div>
  <p class="tagline">Cura e reintegrazione dei capelli</p>
  <div class="web-pill">www.veltrona.it</div>

  <svg class="mascot" viewBox="0 0 260 480" role="img" aria-label="Cartoon mascot: a hair strand doctor in a white coat giving a thumbs up, standing on a peach shadow">
    <defs>
      <linearGradient id="mascot-tone" x1="0" y1="0" x2="0" y2="1">
        <stop offset="0" stop-color="#7a4524"/>
        <stop offset="0.55" stop-color="#b89a86"/>
        <stop offset="1" stop-color="#e7a57a"/>
      </linearGradient>
    </defs>
    <rect x="0" y="0" width="260" height="480" rx="30" fill="url(#mascot-tone)"/>
  </svg>

  <p class="doctor-name">dr. Veltrona</p>
</section>

</body>
</html>
```